Where Quiet Waters Bend

I have a previously designed book cover, and although I am mostly happy with it, I do not care for the photo on the cover of the book. I would like to keep the fonts and scrollwork on the current book cover (the brown outer edge is optional).
I prefer a Christian focus with a soft, gentle, grieving, trusting feeling of a mother as God leads without the typical religious symbols (ie: huge hands, overwhelming crosses, Heaven opening). Softly toned or small Christian icons would be acceptable.
The book dimensions are 5.5 X 8.5 and the spine is 1/2" thick.
Original book cover is here: http://wherequietwatersbend.pagenookhost.net/p/free-books.html
Back cover book description (two photos and the logo for the back cover can be found below) :
For I am the Lord your God who takes hold of your right hand and says to you, "Do not fear, I will help you." Isaiah 41:13
One day you were here, Colby, the next you were at the throne of God. How I long to know what heaven is like so I can envision where you are. Are you talking to Gideon about the battles of old? Are you asking Paul about the stonings, the scales, and the shipwrecks? Or are you still just standing in awe of the God and Savior that your mother could never have come close to describing to you? How I long to stand in awe with you, praising the God who gives and takes away. Just like I told you all those times when you were here with us, "If you go first, I'll see you when I get there, my son." Love you, Mom
On Friday, February 18, 2011, God did the unthinkable in our lives: He chose to take our 12-year-old son, Colby, home to heaven in a skiing accident. It is only considered the unthinkable because our plans are not God's plans and our ways are not God's ways. Follow along on my journey through the valley of the shadow of death as my Savior, Jesus Christ, leads me.
(Author info)
Janna L. Brockwood lives on a small farm in northern Wisconsin with her husband, Dale, and their children. Experiencing the tragic death of her son has caused her to draw closer to God as He leads her down an unexpected path to know Him better.
I have updated the back cover details to include the exact words for the back cover as well as two photos and a logo. Thank you, designers, for sharing your creativity!
Reason: Still looking for the perfect book cover!
Reason: Still looking for the perfect design!
Working on final revisions!

```html
<!DOCTYPE html>
<html lang="en">
<head>
<meta charset="utf-8">
<title>Where Quiet Waters Bend – Book Cover</title>
<link rel="stylesheet" href="https://fonts.googleapis.com/css2?family=Pinyon+Script&family=Cinzel:wght@400&family=Tinos:ital,wght@0,400;0,700;1,700&display=swap">
<style>
  :root {
    --page-bg: #f4f4f4;
    --border-dark: #5a3a1c;
    --border-mid: #8a5e2e;
    --parchment-light: #fbf0d6;
    --parchment: #f0d9a8;
    --parchment-deep: #d9b57a;
    --title-gold: #a67524;
    --author-cream: #fff5e0;
    --ink: #2b2118;
    --glow: #fff7e2;
    --photo-sepia: #9b8468;
  }
  * { margin: 0; padding: 0; box-sizing: border-box; }
  html, body { width: 1200px; height: 1000px; overflow: hidden; }
  body {
    background: radial-gradient(ellipse at center, #ffffff 0%, var(--page-bg) 70%, #e6e6e6 100%);
    position: relative;
  }
  .book {
    position: absolute;
    top: 191px;
    left: 190px;
    display: flex;
    gap: 20px;
  }
  .cover {
    position: relative;
    width: 400px;
    height: 618px;
    background:
      radial-gradient(ellipse at 30% 20%, rgba(160,110,55,.6), transparent 60%),
      radial-gradient(ellipse at 70% 85%, rgba(70,40,15,.7), transparent 60%),
      linear-gradient(135deg, var(--border-mid), var(--border-dark));
    overflow: hidden;
  }
  .cover-inner {
    position: absolute;
    inset: 18px;
    background:
      radial-gradient(ellipse at 50% 45%, var(--parchment-light) 0%, var(--parchment) 55%, var(--parchment-deep) 100%);
  }

  /* Front */
  .front .cover-inner { bottom: 64px; }
  .front-art {
    position: absolute;
    left: 40px; right: 0; top: 170px; bottom: 0;
    background: radial-gradient(ellipse at 55% 45%, var(--glow) 0%, rgba(246,220,170,.8) 40%, rgba(230,190,130,0) 75%);
  }
  .title {
    position: absolute;
    top: 48px; left: 0; right: 0;
    text-align: center;
    font-family: "Pinyon Script", cursive;
    font-size: 46px;
    line-height: 1.05;
    color: var(--title-gold);
    text-shadow: 0 1px 1px rgba(255,250,230,.6);
  }
  .author {
    position: absolute;
    left: 0; right: 0; bottom: 22px;
    text-align: center;
    font-family: "Cinzel", serif;
    font-size: 16px;
    letter-spacing: 5px;
    color: var(--author-cream);
  }

  /* Back */
  .back .cover-inner {
    padding: 50px 14px 0 14px;
    background: linear-gradient(180deg, #f3e1b8, #ead09b 60%, #e0bf85);
    color: var(--ink);
    font-family: "Tinos", serif;
  }
  .verse {
    font-weight: 700;
    font-style: italic;
    font-size: 11px;
    line-height: 1.3;
    text-align: center;
    margin-bottom: 16px;
  }
  .story {
    font-size: 10.3px;
    line-height: 1.3;
    text-align: left;
  }
  .story p + p { margin-top: 12px; }
  .son-photo {
    float: right;
    width: 104px;
    height: 122px;
    margin: 0 0 6px 10px;
    border: 2px solid #3a2a1a;
    background: linear-gradient(160deg, #b9a384, var(--photo-sepia) 60%, #6e5a42);
  }
  .about {
    position: absolute;
    left: 30px; right: 30px; top: 402px;
    height: 112px;
    display: flex;
    gap: 10px;
    padding: 8px;
    background: linear-gradient(90deg, #fff4d4, #fbe8b6);
  }
  .author-photo {
    flex: 0 0 78px;
    height: 94px;
    border: 1px solid #3a2a1a;
    background: linear-gradient(160deg, #c1ad8e, var(--photo-sepia) 60%, #6e5a42);
  }
  .about h2 {
    font-family: "Tinos", serif;
    font-weight: 700;
    font-size: 13px;
    margin-bottom: 2px;
  }
  .about p { font-size: 9.4px; line-height: 1.25; }
  .imprint {
    position: absolute;
    left: 50%; top: 532px;
    transform: translateX(-50%);
    display: flex;
    align-items: center;
    gap: 5px;
    padding: 4px 6px;
    background: #f6e2ad;
    border: 1px solid #3a2a1a;
    font-family: "Tinos", serif;
    font-weight: 700;
    font-size: 8.5px;
    line-height: 1.1;
    text-transform: uppercase;
    text-align: center;
  }
  .imprint-mark { width: 8px; height: 8px; background: var(--ink); }
</style>
</head>
<body>
  <main class="book">
    <section class="cover front">
      <div class="cover-inner">
        <div class="front-art" role="img" aria-label="Soft glowing photograph of gently open hands reaching upward"></div>
        <h1 class="title">Where Quiet<br>Waters Bend</h1>
      </div>
      <p class="author">Janna L. Brockwood</p>
    </section>

    <section class="cover back">
      <div class="cover-inner">
        <p class="verse">For I am the Lord your God who takes hold of your right hand and says to you, "Do not fear, I will help you." Isaiah 41:13</p>
        <div class="story">
          <div class="son-photo" role="img" aria-label="Sepia portrait photo of the author's son"></div>
          <p>One day you were here, Colby, the next you were at the throne of God. How I long to know what heaven is like so I can envision where you are. Are you talking to Gideon about the battles of old? Are you asking Paul about the stonings, the scales, and the shipwrecks? Or are you still just standing in awe of the God and Savior that your mother could never have come close to describing to you? How I long to stand in awe with you, praising the God who gives and takes away. Just like I told you all those times when you were here with us, "If you go first, I'll see you when I get there, my son." Love you, Mom</p>
          <p>On Friday, February 18, 2011, God did the unthinkable in our lives: He chose to take our 12-year-old son, Colby, home to heaven in a skiing accident. It is only considered the unthinkable because our plans are not God's plans and our ways are not God's ways. Follow along on my journey through the valley of the shadow of death as my Savior, Jesus Christ, leads me.</p>
        </div>
        <aside class="about">
          <div class="author-photo" role="img" aria-label="Sepia portrait photo of the author"></div>
          <div>
            <h2>ABOUT THE AUTHOR</h2>
            <p>Janna L. Brockwood lives on a small farm in northern Wisconsin with her husband, Dale, and their children. Experiencing the tragic death of her son has caused her to draw closer to God as He leads her down an unexpected path to know Him better.</p>
          </div>
        </aside>
        <div class="imprint"><span class="imprint-mark"></span><span>Still Harbor<br>Ministries</span></div>
      </div>
    </section>
  </main>
</body>
</html>
```